Mobile app for deals

Mobile App Name: Bid 2 Pact

Design screen shots for the issue of quotes for deals.

1. Loading screen
2. User signs in with credentials or signs up
2. Search by category
3. Search by location
4. Create a project

The expected experience after a project is placed:
- Project alerted
- Quotes
- Project complete
- Rating
- Payment

#TotallyExcited
Updates

Project Deadline Extended Reason: Deadline has been extended on request from a few designers who saw the project late and who would like to submit designs.Thank you to all who submitted on time, we are reviewing your designs and will respond shortly. Added Monday, June 29, 2015

Target Market(s)

Contractors market

Industry/Entity Type

Business Directory

Font styles to use
Sans Serif

Requirements
Must have
• Simple design
• User friendly
• Translateable (later)

```html
<!DOCTYPE html>
<html lang="en">
<head>
<meta charset="utf-8">
<title>Bid 2 Pact – App Screens</title>
<link rel="stylesheet" href="https://fonts.googleapis.com/css2?family=Roboto+Slab:wght@300&family=PT+Sans+Narrow:wght@400;700&display=swap">
<style>
:root{
  --bg:#ffffff;
  --heading:#4a4646;
  --caption:#5a5656;
  --status:#f2f2f2;
  --green:#55b25d;
  --green-dark:#3f9b48;
  --slate:#3b3f49;
  --red:#e2533d;
  --red-dark:#c8412d;
  --social-a:#d84c36;
  --social-b:#4a9fd4;
  --social-c:#3d5a98;
  --yellow-top:#f8c546;
  --yellow-bottom:#fbee7a;
  --orange:#f0a032;
  --ink:#3a2d1e;
  --teal:#48b18b;
  --teal-dark:#379877;
  --white:#ffffff;
  --field-text:#888888;
}
*{box-sizing:border-box;margin:0;padding:0}
html,body{width:1200px;height:927px;overflow:hidden;background:var(--bg)}
.board{position:relative;width:1200px;height:927px;font-family:"Roboto Slab",Georgia,serif}
.board-title{position:absolute;left:38px;top:34px;font-family:"PT Sans Narrow",Arial,sans-serif;font-weight:400;font-size:58px;line-height:70px;color:var(--heading)}
.screen{position:absolute;top:198px;width:157px;height:235px;overflow:hidden;font-family:"PT Sans Narrow",Arial,sans-serif;color:var(--white)}
.status-bar{position:absolute;left:0;top:0;width:100%;height:10px;background:var(--status);color:#333;font-size:6px;line-height:10px;font-family:Arial,sans-serif;font-weight:bold}
.status-bar .carrier{position:absolute;left:6px}
.status-bar .time{position:absolute;left:0;right:0;text-align:center}
.status-bar .battery{position:absolute;right:5px;top:3px;width:10px;height:4px;border:1px solid #555}
.band{position:absolute;left:0;width:100%;text-align:center;font-weight:700;white-space:nowrap}
.abs{position:absolute}
.field{position:absolute;background:var(--white);color:var(--field-text);font-size:8px;padding:3px 5px;line-height:12px}
.chev{position:absolute;right:5px;top:3px;width:8px;height:8px}
.caption{position:absolute;top:521px;width:160px;font-weight:300;font-size:15.5px;line-height:20px;color:var(--caption)}
.caption p+p{margin-top:20px}

.splash{left:39px;background:var(--green)}
.splash .account-links{top:15px;right:8px;font-size:9.5px;line-height:12px}
.splash .band{background:var(--green-dark);font-size:11px;line-height:19px}
.splash .grab-ring{left:51px;top:94px;width:56px;height:56px;border:5px solid var(--white);border-radius:50%}
.splash .grab-line{left:59px;top:158px;width:40px;height:1.5px;background:var(--green-dark)}

.signin{left:280px;background:var(--slate)}
.signin .brand-mark{left:8px;top:18px;width:25px;height:25px;border:2px solid var(--white);border-radius:50%}
.signin .brand-name{left:42px;top:22px;font-size:14px;line-height:16px}
.signin .email{left:13px;top:72px;width:112px;height:23px;line-height:17px}
.signin .confirm{left:130px;top:77px;width:14px;height:14px;border:1.5px solid var(--white)}
.social{position:absolute;left:13px;width:130px;height:24px;font-size:9px;line-height:24px;padding-left:30px}
.social .mark{position:absolute;left:6px;top:6px;width:12px;height:12px;background:rgba(255,255,255,.85)}
.social-a{top:127px;background:var(--social-a)}
.social-b{top:162px;background:var(--social-b)}
.social-c{top:197px;background:var(--social-c)}

.app-header{position:absolute;left:0;top:10px;width:100%;height:20px;font-size:7px;line-height:20px}
.app-header .mini-mark{position:absolute;left:5px;top:5px;width:10px;height:10px;border-radius:50%;background:var(--white)}
.app-header .mini-name{position:absolute;left:18px}
.app-header .greeting{position:absolute;right:6px;font-weight:700;font-size:8.5px}
.home-icon{position:absolute;left:9px;top:212px;width:15px;height:15px}

.create{left:520px;background:var(--red)}
.create .band{top:30px;height:20px;line-height:20px;background:var(--red-dark);font-size:12.5px}

.accepted{left:760px;top:208px;height:225px;background:linear-gradient(180deg,var(--yellow-top),var(--yellow-bottom));color:var(--ink)}
.accepted .headline{top:18px;width:100%;text-align:center;font-weight:700;font-size:21px;line-height:26px}
.accepted .seal{left:36px;top:60px;width:86px;height:86px;border-radius:50%;border:6px solid var(--orange)}
.accepted .message{top:186px;width:100%;text-align:center;font-weight:700;font-size:13px;line-height:16px}

.profile{left:1004px;background:var(--teal)}
.profile .band{top:30px;height:20px;line-height:20px;background:var(--teal-dark);font-size:12.5px}
.profile .avatar{left:51px;top:59px;width:56px;height:56px;border-radius:50%;border:3px solid #e6e6e6;background:linear-gradient(180deg,#e3683a 0%,#f2c6a4 60%,#3b3f49 100%)}
.profile .story{left:21px;top:126px;width:112px;height:70px;overflow:hidden;font-size:7.5px;line-height:12.5px}
.profile .story b{font-weight:700}
.profile .more{left:134px;top:180px;width:7px;height:7px}
</style>
</head>
<body>
<main class="board">
  <h1 class="board-title">Bid 2 Pact</h1>

  <section class="screen splash">
    <div class="status-bar"><span class="carrier">Carrier</span><span class="time">12:00 PM</span><span class="battery"></span></div>
    <div class="abs account-links">Sign In &nbsp;|&nbsp; Register</div>
    <div class="band" style="top:30px">Professional looking for work?</div>
    <div class="abs grab-ring"></div>
    <div class="abs grab-line"></div>
    <div class="band" style="top:196px">I need a professional for work!</div>
  </section>

  <section class="screen signin">
    <div class="status-bar"><span class="carrier">Carrier</span><span class="time">12:00 PM</span><span class="battery"></span></div>
    <div class="abs brand-mark"></div>
    <div class="abs brand-name">Bid 2 Pact</div>
    <div class="field email">Email?</div>
    <div class="abs confirm"></div>
    <div class="social social-a"><span class="mark"></span>Sign in with Nimbus</div>
    <div class="social social-b"><span class="mark"></span>Sign in with Chatter</div>
    <div class="social social-c"><span class="mark"></span>Sign in with Friendly</div>
  </section>

  <section class="screen create">
    <div class="status-bar"><span class="carrier">Carrier</span><span class="time">12:00 PM</span><span class="battery"></span></div>
    <div class="app-header"><span class="mini-mark"></span><span class="mini-name">Bid 2 Pact</span><span class="greeting">Hi, Nora M.</span></div>
    <div class="band">Create a Project</div>
    <div class="field" style="left:13px;top:65px;width:130px;height:18px">Project Name</div>
    <div class="field" style="left:13px;top:89px;width:130px;height:36px">Project Description</div>
    <div class="field" style="left:20px;top:137px;width:116px;height:17px">Industry
      <svg class="chev" viewBox="0 0 8 8"><path d="M1 3l3 3 3-3" fill="none" stroke="#999" stroke-width="1"/></svg></div>
    <div class="field" style="left:20px;top:161px;width:96px;height:18px">When?</div>
    <svg class="abs" style="left:119px;top:161px" width="17" height="18" viewBox="0 0 17 18">
      <rect x="0" y="0" width="17" height="18" fill="#fff"/>
      <rect x="2" y="3" width="13" height="13" fill="none" stroke="#e2533d" stroke-width="1.2"/>
      <g fill="#e2533d"><rect x="4" y="7" width="2" height="2"/><rect x="7.5" y="7" width="2" height="2"/><rect x="11" y="7" width="2" height="2"/><rect x="4" y="11" width="2" height="2"/><rect x="7.5" y="11" width="2" height="2"/><rect x="11" y="11" width="2" height="2"/></g>
    </svg>
    <div class="field" style="left:48px;top:194px;width:95px;height:18px">Status
      <svg class="chev" viewBox="0 0 8 8"><path d="M1 3l3 3 3-3" fill="none" stroke="#999" stroke-width="1"/></svg></div>
    <svg class="home-icon" viewBox="0 0 16 16"><path d="M2 8L8 2l6 6M4 6.5V14h3v-4h2v4h3V6.5" fill="none" stroke="#fff" stroke-width="1.4"/></svg>
  </section>

  <section class="screen accepted">
    <div class="abs headline">Congratulations!</div>
    <div class="abs seal"></div>
    <div class="abs message">Your quote was accepted</div>
  </section>

  <section class="screen profile">
    <div class="status-bar"><span class="carrier">Carrier</span><span class="time">12:00 PM</span><span class="battery"></span></div>
    <div class="app-header"><span class="mini-mark"></span><span class="mini-name">Bid 2 Pact</span><span class="greeting">Hi, Nora M.</span></div>
    <div class="band">My profile</div>
    <div class="abs avatar" role="img" aria-label="Illustrated avatar of the member"></div>
    <p class="abs story">Hey, Nora, you've been a member since April 6th and have 3 active projects. Two projects were completed in May, which is super cool! Click <b>here</b> to update your profile. Here's the email</p>
    <svg class="abs more" viewBox="0 0 8 8"><path d="M1 3l3 3 3-3" fill="none" stroke="#fff" stroke-width="1"/></svg>
    <svg class="home-icon" viewBox="0 0 16 16"><path d="M2 8L8 2l6 6M4 6.5V14h3v-4h2v4h3V6.5" fill="none" stroke="#fff" stroke-width="1.4"/></svg>
  </section>

  <div class="caption" style="left:39px;width:158px"><p>UX: User selects and holds logo icon in the middle and drags up or down to selection.</p></div>
  <div class="caption" style="left:280px;width:155px"><p>UX: Integration with social media signin makes for an optimized user experience. Option to use proprietary signin is presented first. Once email is inputted and box selected, the password prompt appears.</p></div>
  <div class="caption" style="left:520px;width:158px"><p>UX: Status pull down menu reveals options to cancel, submit, update, etc.</p><p>Selecting the home icon takes user back to all projects. Transition is a screen swipe.</p></div>
  <div class="caption" style="left:1004px;width:150px"><p>UX: A running narrative that tells the user a story, instead of bulleted information about their profile. Interactive…</p></div>
</main>
</body>
</html>
```